Real Estate Investing company needs a business card design

We need a business card design for new Real Estate Investment Company called "Maple Ridge Ventures, LLC." We buy homes for cash and close quickly in any situation. Our company provides an easy and fast option for home owners who are in tough situations who need to sell their home fast and don't want realtor fees or other listing hassles. We also renovate and resell our homes which helps provide housing for the community. We would like to see designs that use the colors blue and white to match our company logo or other colors that may match our company logo. The final design should communicate trust and easy process.
Industry/Entity Type
Business
Contact Information for Business Card
Front should have company name and company logo. back of card should have company logo and area to list services.
Look and feel

```html
<!DOCTYPE html>
<html lang="en">
<head>
<meta charset="utf-8">
<title>Maple Ridge Ventures – Business Card</title>
<link href="https://fonts.googleapis.com/css2?family=Open+Sans:wght@400;600;700&family=Exo+2:wght@700&display=swap" rel="stylesheet">
<style>
  :root {
    --brand-blue: #1f78c8;
    --brand-blue-dark: #155a9e;
    --brand-blue-light: #3d93dc;
    --paper: #ffffff;
    --stage: #ecedef;
    --ink-light: #eaf3fb;
  }
  * { box-sizing: border-box; margin: 0; padding: 0; }
  html, body { width: 1200px; height: 843px; overflow: hidden; }
  body {
    background: var(--stage);
    font-family: "Open Sans", Arial, sans-serif;
    position: relative;
  }
  .card {
    position: absolute;
    width: 520px;
    height: 297px;
    top: 273px;
    border-radius: 4px;
    overflow: hidden;
    box-shadow: 0 10px 28px rgba(0,0,0,.18);
  }
  /* Back of card */
  .card-back {
    left: 50px;
    background: linear-gradient(135deg, var(--brand-blue-light), var(--brand-blue) 55%, var(--brand-blue-dark));
    color: var(--paper);
    padding: 40px 36px;
  }
  .brand-mark {
    display: flex;
    align-items: center;
    gap: 10px;
    font-family: "Exo 2", Arial, sans-serif;
    font-weight: 700;
    text-transform: uppercase;
    line-height: 1.05;
  }
  .brand-mark .brand-square {
    width: 30px; height: 30px; flex: none;
  }
  .card-back .brand-mark { color: var(--paper); font-size: 26px; }
  .card-back .brand-square { background: var(--paper); }
  .services {
    list-style: none;
    margin-top: 28px;
    font-size: 12.5px;
    line-height: 1.45;
  }
  .services li {
    position: relative;
    padding-left: 16px;
    margin-bottom: 8px;
  }
  .services li::before {
    content: "";
    position: absolute;
    left: 2px; top: 7px;
    width: 5px; height: 5px;
    border-radius: 50%;
    background: var(--paper);
  }
  /* Front of card */
  .card-front {
    left: 630px;
    background: var(--paper);
  }
  .front-panel { position: absolute; inset: 0; }
  .card-front .brand-mark {
    position: absolute;
    left: 34px; top: 112px;
    width: 230px;
    color: var(--brand-blue);
    font-size: 24px;
  }
  .card-front .brand-square { background: var(--brand-blue); }
  .contact {
    position: absolute;
    left: 318px; top: 40px;
    right: 14px;
    color: var(--paper);
  }
  .contact-name { font-size: 19px; font-weight: 700; }
  .contact-title { font-size: 13px; font-weight: 600; margin-bottom: 22px; }
  .contact-address { font-size: 12.5px; line-height: 1.4; margin-bottom: 6px; }
  .contact-row {
    display: flex; align-items: center; gap: 8px;
    font-size: 12px; line-height: 1.75;
    white-space: nowrap;
  }
  .contact-row svg { width: 12px; height: 12px; flex: none; fill: var(--ink-light); }
</style>
</head>
<body>

<section class="card card-back" aria-label="Back of business card">
  <div class="brand-mark"><span class="brand-square"></span><span>Maple Ridge Ventures</span></div>
  <ul class="services">
    <li>We buy homes for cash &amp; close quickly in any situation.</li>
    <li>Easy &amp; fast option for home owners who need to sell their home fast &amp; also avoid realtor fees &amp; listing hassles.</li>
    <li>We also renovate &amp; resell!</li>
  </ul>
</section>

<section class="card card-front" aria-label="Front of business card">
  <svg class="front-panel" viewBox="0 0 520 297" preserveAspectRatio="none" aria-hidden="true">
    <defs>
      <linearGradient id="panelFill" x1="0" y1="0" x2="1" y2="1">
        <stop offset="0" stop-color="#3d93dc"/>
        <stop offset="1" stop-color="#155a9e"/>
      </linearGradient>
    </defs>
    <path d="M300 0 H520 V297 H300 V52 L290 44 L300 36 Z" fill="url(#panelFill)"/>
  </svg>

  <div class="brand-mark"><span class="brand-square"></span><span>Maple Ridge Ventures</span></div>

  <div class="contact">
    <div class="contact-name">Daniel Reyes</div>
    <div class="contact-title">CEO/Founder</div>
    <div class="contact-address">2140 Birchwood Lane<br>Juneau, Alaska 99801</div>
    <div class="contact-row">
      <svg viewBox="0 0 24 24"><path d="M6.6 10.8a15 15 0 0 0 6.6 6.6l2.2-2.2a1 1 0 0 1 1-.25 11.4 11.4 0 0 0 3.6.57 1 1 0 0 1 1 1V20a1 1 0 0 1-1 1A17 17 0 0 1 3 4a1 1 0 0 1 1-1h3.5a1 1 0 0 1 1 1c0 1.25.2 2.45.57 3.57a1 1 0 0 1-.25 1z"/></svg>
      <span>555 013 2847</span>
    </div>
    <div class="contact-row">
      <svg viewBox="0 0 24 24"><path d="M6 2h12v5H6zM4 8h16a2 2 0 0 1 2 2v7h-4v5H6v-5H2v-7a2 2 0 0 1 2-2zm4 9v3h8v-3z"/></svg>
      <span>555 017 6391</span>
    </div>
    <div class="contact-row">
      <svg viewBox="0 0 24 24"><path d="M2 5h20v14H2zm2 2v.5l8 5 8-5V7z"/></svg>
      <span>hello@mapleridgeventures.com</span>
    </div>
    <div class="contact-row">
      <svg viewBox="0 0 24 24"><circle cx="12" cy="12" r="10"/></svg>
      <span>www.mapleridgeventures.com</span>
    </div>
  </div>
</section>

</body>
</html>
```